Design for sports training app

We need the design for 9 screens of an app that supports trainers of sport teams in preparing their training sessions. Regarding colors, fonts etc. there is absolute freedom for the designer to choose what he thinks is best.
The app will be called "Vellix", our idea for the logo is something like a stopwatch.
Wireframes are attached for every screen. You don't have to stick to those - if you have better ideas, we are happy to see them.
Our strategy is "mobile first". Based on the app design we will create a homepage later - I guess it makes sense to give this to the same person, let's see.
The deliverables are attached.
All in all the main target is to present a very simple, intuitive and nice UI that the user can work with without much learning.
Updates
Target Market(s)
Soccer trainers
Industry/Entity Type
Training
Look and feel

```html
<!DOCTYPE html>
<html lang="en">
<head>
<meta charset="utf-8">
<title>Vellix – Sign In and Session Overview</title>
<link href="https://fonts.googleapis.com/css2?family=Open+Sans:wght@400;600;700&family=Mulish:wght@400;600;800&display=swap" rel="stylesheet">
<style>
  :root {
    --brand: #03a9f4;
    --brand-dark: #0896d6;
    --ink: #222;
    --line: #dcdcdc;
    --white: #fff;
    --canvas: #fff;
    --photo-top: #6d7378;
    --photo-mid: #3f5a2c;
    --photo-low: #6c8a2e;
  }
  * { box-sizing: border-box; margin: 0; padding: 0; }
  html, body { width: 1200px; height: 1037px; overflow: hidden; background: var(--canvas); }
  .stage { position: relative; width: 1430px; height: 1236px; transform: scale(0.8392); transform-origin: 0 0; }
  .screen { position: absolute; top: 50px; width: 640px; height: 1135px; overflow: hidden; box-shadow: 0 2px 12px rgba(0,0,0,.18); }
  .screen--login { left: 50px; font-family: "Open Sans", sans-serif; color: var(--white); }
  .screen--session { left: 740px; background: var(--white); font-family: "Mulish", sans-serif; color: var(--ink); }

  .status-bar { position: absolute; top: 0; left: 0; right: 0; height: 40px; display: flex; align-items: center; justify-content: center; color: var(--white); font: 400 22px "Mulish", sans-serif; z-index: 2; }
  .status-bar .signal { position: absolute; left: 12px; top: 11px; }
  .status-bar .battery { position: absolute; right: 12px; top: 11px; }

  .hero-photo { position: absolute; inset: 0; background: linear-gradient(180deg, var(--photo-top) 0%, #4b5a4a 18%, var(--photo-mid) 45%, var(--photo-low) 72%, #4a5a22 100%); }
  .app-title { position: absolute; top: 238px; width: 100%; text-align: center; font-weight: 700; font-size: 66px; letter-spacing: 1px; }
  .field { position: absolute; left: 70px; width: 500px; border-bottom: 1px solid rgba(255,255,255,.85); text-align: center; font-size: 28px; padding-bottom: 12px; }
  .field--user { top: 560px; }
  .field--pass { top: 658px; }
  .forgot { position: absolute; top: 758px; width: 100%; text-align: center; font-size: 22px; }
  .sign-in { position: absolute; left: 70px; top: 912px; width: 500px; height: 88px; border-radius: 6px; background: var(--brand); display: flex; align-items: center; justify-content: center; font-weight: 700; font-size: 28px; letter-spacing: 1.5px; }
  .sign-up { position: absolute; top: 1044px; width: 100%; text-align: center; font-size: 22px; }
  .sign-up strong { font-weight: 700; }

  .app-header { position: absolute; top: 0; left: 0; right: 0; height: 123px; background: var(--brand); }
  .team-name { position: absolute; top: 62px; width: 100%; text-align: center; color: var(--white); font-weight: 800; font-size: 29px; }
  .settings { position: absolute; right: 28px; top: 58px; }
  .info-row { position: absolute; top: 123px; left: 0; right: 0; height: 131px; border-bottom: 1px solid var(--line); display: flex; }
  .info-cell { flex: 1; display: flex; align-items: center; gap: 20px; padding-left: 28px; font-size: 27px; line-height: 38px; letter-spacing: .5px; }
  .info-cell + .info-cell { border-left: 1px solid var(--line); }
  .start-area { position: absolute; top: 254px; left: 0; right: 0; height: 303px; border-bottom: 1px solid var(--line); }
  .start-button { position: absolute; left: 193px; top: 25px; width: 254px; height: 254px; border-radius: 50%; background: var(--brand); border: 3px solid var(--brand-dark); display: flex; align-items: center; justify-content: center; }
  .drill-list { position: absolute; top: 557px; left: 0; right: 0; list-style: none; }
  .drill { height: 96.5px; border-bottom: 1px solid var(--line); display: flex; align-items: center; justify-content: space-between; padding: 0 31px 0 29px; font-size: 23px; letter-spacing: .3px; }
  .drill:last-child { border-bottom: 0; }
  .duration { width: 98px; height: 50px; border-radius: 6px; background: var(--brand); color: var(--white); font-weight: 600; font-size: 24px; display: flex; align-items: center; justify-content: center; letter-spacing: .5px; }
</style>
</head>
<body>
<div class="stage">

  <section class="screen screen--login">
    <div class="hero-photo" role="img" aria-label="Photo of a player in a red shirt kicking a ball on a sunny field in front of a forest"></div>
    <div class="status-bar">
      <svg class="signal" width="100" height="18" viewBox="0 0 100 18"><g fill="#fff"><circle cx="6" cy="9" r="5"/><circle cx="19" cy="9" r="5"/><circle cx="32" cy="9" r="5"/><circle cx="45" cy="9" r="5"/></g><circle cx="58" cy="9" r="4.5" fill="none" stroke="#fff" stroke-width="1.2"/><path d="M80 6a14 14 0 0 1 20 0M83 9.5a9 9 0 0 1 14 0M86.5 13a4 4 0 0 1 7 0" stroke="#fff" stroke-width="2.4" fill="none" stroke-linecap="round"/></svg>
      4:21 PM
      <svg class="battery" width="50" height="18" viewBox="0 0 50 18"><rect x="1" y="1" width="44" height="16" rx="2.5" fill="#fff" stroke="#fff"/><rect x="46" y="6" width="3" height="6" fill="#fff"/></svg>
    </div>
    <h1 class="app-title">Strivo</h1>
    <div class="field field--user">Username</div>
    <div class="field field--pass">Password</div>
    <div class="forgot">Forgot password?</div>
    <div class="sign-in">SIGN IN</div>
    <div class="sign-up">New user? <strong>Sign Up</strong></div>
  </section>

  <section class="screen screen--session">
    <header class="app-header">
      <div class="status-bar">
        <svg class="signal" width="100" height="18" viewBox="0 0 100 18"><g fill="#fff"><circle cx="6" cy="9" r="5"/><circle cx="19" cy="9" r="5"/><circle cx="32" cy="9" r="5"/><circle cx="45" cy="9" r="5"/></g><circle cx="58" cy="9" r="4.5" fill="none" stroke="#fff" stroke-width="1.2"/><path d="M80 6a14 14 0 0 1 20 0M83 9.5a9 9 0 0 1 14 0M86.5 13a4 4 0 0 1 7 0" stroke="#fff" stroke-width="2.4" fill="none" stroke-linecap="round"/></svg>
        4:21 PM
        <svg class="battery" width="50" height="18" viewBox="0 0 50 18"><rect x="1" y="1" width="44" height="16" rx="2.5" fill="#fff" stroke="#fff"/><rect x="46" y="6" width="3" height="6" fill="#fff"/></svg>
      </div>
      <h2 class="team-name">FC Lindental - Juniors</h2>
      <svg class="settings" width="48" height="48" viewBox="0 0 48 48" fill="none" stroke="#fff" stroke-width="2.6" stroke-linejoin="round">
        <path d="M20 3h8l1.5 6 4.5 2.5 6-2 4 7-4.5 4.3v5.4l4.5 4.3-4 7-6-2-4.5 2.5-1.5 6h-8l-1.5-6-4.5-2.5-6 2-4-7 4.5-4.3v-5.4L3.5 16.5l4-7 6 2 4.5-2.5z"/>
        <circle cx="24" cy="24" r="6.5"/>
      </svg>
    </header>

    <div class="info-row">
      <div class="info-cell">
        <svg width="72" height="72" viewBox="0 0 72 72" fill="none" stroke="#222" stroke-width="4"><circle cx="36" cy="36" r="33"/><path d="M36 16v21h14" stroke-linecap="round"/></svg>
        <span>Sep 15,<br>2016</span>
      </div>
      <div class="info-cell">
        <svg width="74" height="72" viewBox="0 0 74 72" fill="none" stroke="#222" stroke-width="3.6" stroke-linecap="round"><path d="M42 4v5M26 10l3 3M58 10l-3 3M66 27h-5"/><path d="M32 30a13 13 0 0 1 25 6"/><path d="M14 68h40a11 11 0 0 0 0-22 15 15 0 0 0-29-2 12 12 0 0 0-11 24z"/></svg>
        <span>Clear<br>22°</span>
      </div>
    </div>

    <div class="start-area">
      <div class="start-button" aria-label="Start training">
        <svg width="100" height="92" viewBox="0 0 100 92" fill="none" stroke="#fff" stroke-width="4" stroke-linejoin="round" stroke-linecap="round">
          <path d="M22 18 34 4l10 10 14 20 14 8 18 6 4 8v16H40L20 40z"/>
          <path d="M46 32l6-6M52 42l6-6M62 64h32"/>
          <path d="M2 52h18M8 64h18M16 76h16"/>
        </svg>
      </div>
    </div>

    <ul class="drill-list">
      <li class="drill"><span>Warm-Up</span><span class="duration">20:00</span></li>
      <li class="drill"><span>4 vs. 2</span><span class="duration">25:00</span></li>
      <li class="drill"><span>Offensive (2 vs.1)</span><span class="duration">25:00</span></li>
      <li class="drill"><span>Game 7 on 7</span><span class="duration">50:00</span></li>
      <li class="drill"><span>Vellix Skills</span><svg width="14" height="24" viewBox="0 0 14 24" fill="none" stroke="#555" stroke-width="1.8"><path d="M2 2l10 10-10 10"/></svg></li>
      <li class="drill"><span>Prerequisites</span><svg width="14" height="24" viewBox="0 0 14 24" fill="none" stroke="#555" stroke-width="1.8"><path d="M2 2l10 10-10 10"/></svg></li>
    </ul>
  </section>

</div>
</body>
</html>
```